Branding pakage with new logo

Hi everyone, we just rebranded and i need a complete branding pakage that will flow together with everything.

Trevik 2500 vehicle wrap
Halvor stridex van wrap
2025 k270 wrap
16x8 enclosed trailer wrap
Business cards
Yard signs
Signage on building
Polo and t shirts for employees

Target Market(s)

Custom Window and door market

Industry/Entity Type

Window's doors and garage doors

Colors

Designer to choose colors to be used in the design.

```html
<!DOCTYPE html>
<html lang="en">
<head>
<meta charset="utf-8">
<title>Kestrel Doors – Business Card</title>
<link rel="stylesheet" href="https://fonts.googleapis.com/css2?family=Exo+2:wght@600;700&family=Montserrat:wght@400;500&display=swap">
<style>
  :root {
    --backdrop: #1d1d1e;
    --card-white: #ffffff;
    --brand-orange: #e8561f;
    --brand-charcoal: #2b2b2b;
    --text-grey: #4a4a4a;
    --rule-grey: #7a7a7a;
    --back-black: #141414;
    --foil-silver: #d9d9d9;
  }
  * { margin: 0; padding: 0; box-sizing: border-box; }
  html, body {
    width: 1200px; height: 900px; overflow: hidden;
    background: var(--backdrop);
  }
  .canvas { position: relative; width: 1200px; height: 900px; }

  .card {
    position: absolute;
    width: 540px; height: 310px;
    border-radius: 4px;
    box-shadow: 0 18px 40px rgba(0,0,0,.55);
    overflow: hidden;
  }

  /* Back of card */
  .card-back { left: 90px; top: 110px; background: var(--back-black); }
  .back-pattern {
    position: absolute; inset: 0;
    background: linear-gradient(125deg, #6e6e6e 0%, #3a3a3a 22%, #1e1e1e 50%, var(--back-black) 100%);
  }
  .back-mark {
    position: absolute; left: 330px; top: 80px;
    display: flex; align-items: center; gap: 10px;
    padding: 10px 14px;
    background: var(--back-black);
    border: 1px solid #ffffff;
  }
  .back-mark-square { width: 22px; height: 22px; background: var(--brand-orange); }
  .back-mark-name {
    font-family: "Exo 2", sans-serif; font-weight: 700;
    font-size: 18px; letter-spacing: .5px; color: #ffffff;
  }

  /* Front of card */
  .card-front {
    left: 570px; top: 470px;
    background: var(--card-white);
    font-family: "Montserrat", sans-serif;
    color: var(--text-grey);
  }
  .brand {
    position: absolute; right: 34px; top: 40px;
    display: flex; align-items: center; gap: 10px;
  }
  .brand-square { width: 26px; height: 26px; background: var(--brand-orange); }
  .brand-name {
    font-family: "Exo 2", sans-serif; font-weight: 700;
    font-size: 26px; letter-spacing: .5px;
    color: var(--brand-orange);
  }
  .brand-rule {
    position: absolute; right: 34px; top: 86px;
    width: 240px; height: 1px; background: var(--rule-grey);
  }
  .address {
    position: absolute; right: 34px; top: 100px;
    text-align: right; font-size: 14px; line-height: 19px;
    font-style: normal;
  }

  .person { position: absolute; left: 34px; top: 104px; }
  .person-name {
    font-family: "Exo 2", sans-serif; font-weight: 700;
    font-size: 21px; line-height: 25px; color: var(--brand-orange); letter-spacing: .5px;
  }
  .person-title {
    font-family: "Exo 2", sans-serif; font-weight: 600;
    font-size: 15px; line-height: 19px; color: var(--brand-charcoal);
  }
  .person-rule {
    width: 180px; height: 1px; background: var(--rule-grey);
    margin: 9px 0 7px;
  }
  .contact-list { list-style: none; }
  .contact-list li {
    display: flex; align-items: center; gap: 8px;
    font-size: 14px; line-height: 21px;
  }
  .contact-list svg { width: 13px; height: 13px; fill: var(--brand-orange); }

  .swoosh { position: absolute; left: 0; top: 0; width: 540px; height: 310px; }
  .website {
    position: absolute; right: 30px; bottom: 24px;
    font-size: 14px; color: #fff; letter-spacing: .3px;
  }
</style>
</head>
<body>
<main class="canvas">

  <section class="card card-back">
    <div class="back-pattern" role="img" aria-label="Embossed silver foil repeating monogram pattern on black card stock"></div>
    <div class="back-mark">
      <span class="back-mark-square"></span>
      <span class="back-mark-name">KESTREL DOORS</span>
    </div>
  </section>

  <section class="card card-front">
    <svg class="swoosh" viewBox="0 0 540 310" aria-hidden="true">
      <path d="M40,310 C220,262 380,212 540,176 L540,190 C390,224 250,272 100,310 Z" fill="var(--brand-charcoal)"/>
      <path d="M150,310 C290,262 420,226 540,212 L540,310 Z" fill="var(--brand-orange)"/>
    </svg>

    <div class="brand">
      <span class="brand-square"></span>
      <span class="brand-name">KESTREL DOORS</span>
    </div>
    <div class="brand-rule"></div>

    <address class="address">
      412 Larkmoor Road, NE<br>
      Fenwick Bay, MD 20999
    </address>

    <div class="person">
      <p class="person-name">DORIAN VALE</p>
      <p class="person-title">Founder &amp; CEO</p>
      <div class="person-rule"></div>
      <ul class="contact-list">
        <li>
          <svg viewBox="0 0 16 16"><path d="M2 5c0-2 2-3 6-3s6 1 6 3v1h-3V5H5v1H2zM4 7h8l2 7H2z"/></svg>
          555.204.1830
        </li>
        <li>
          <svg viewBox="0 0 16 16"><path d="M4 1h8v14H4zM5.5 3v9h5V3z"/></svg>
          555.617.4402
        </li>
        <li>
          <svg viewBox="0 0 16 16"><path d="M1 4h14v9H1zM2 5l6 4.5L14 5z"/></svg>
          info@kestrelmail.com
        </li>
      </ul>
    </div>

    <p class="website">www.kestreldoors.com</p>
  </section>

</main>
</body>
</html>
```